Business Card Design Project

Need a business card with logo that is attached.
Company name: Tolmen Brisk Solutions, LLC
My name: Lorna Tolmen
Title: President
Phone number: 703-555-0148
Email: ltolmen@tolmenbrisksolutions.example
web site: www.tolmenbrisksolutions.example

Industry/Entity Type

Business

```html
<!DOCTYPE html>
<html lang="en">
<head>
<meta charset="utf-8">
<title>Tolmen Brisk Solutions, LLC — Business Card</title>
<link rel="stylesheet" href="https://fonts.googleapis.com/css2?family=Jost:wght@400;600&display=swap">
<style>
  :root {
    --page-bg: #e9e6e1;
    --card-bg: #4a4644;
    --card-text: #ffffff;
    --brand: #2a8aa6;
    --divider: #2f9a7c;
  }
  html, body {
    margin: 0;
    width: 1200px;
    height: 905px;
    overflow: hidden;
    background: var(--page-bg);
    font-family: "Jost", "Futura", sans-serif;
  }
  .canvas {
    position: relative;
    width: 1200px;
    height: 905px;
    display: flex;
    align-items: center;
    justify-content: center;
  }
  .card {
    position: relative;
    width: 780px;
    height: 780px;
    border-radius: 44px;
    background: var(--card-bg);
    color: var(--card-text);
    box-shadow: 0 6px 18px rgba(0,0,0,0.18);
  }
  .brand {
    position: absolute;
    left: 88px;
    top: 118px;
    display: flex;
    align-items: center;
  }
  .brand-dot {
    width: 150px;
    height: 150px;
    border-radius: 50%;
    background: var(--brand);
    flex: none;
  }
  .brand-divider {
    width: 3px;
    height: 200px;
    background: var(--divider);
    margin: 0 22px 0 26px;
    flex: none;
  }
  .brand-name {
    margin: 0;
    font-size: 40px;
    line-height: 1.12;
    font-weight: 400;
    letter-spacing: 0.04em;
    text-transform: uppercase;
    color: var(--brand);
  }
  .person {
    position: absolute;
    left: 0;
    right: 0;
    top: 420px;
    text-align: center;
    padding-left: 40px;
  }
  .person-name {
    margin: 0;
    font-size: 50px;
    font-weight: 400;
    letter-spacing: 0.01em;
  }
  .person-title {
    margin: 4px 0 0;
    font-size: 28px;
    font-weight: 400;
  }
  .contact {
    position: absolute;
    left: 0;
    right: 0;
    top: 580px;
    text-align: center;
    padding-left: 20px;
  }
  .contact-phone {
    margin: 0 0 6px;
    font-size: 44px;
    font-weight: 600;
    letter-spacing: 0.02em;
  }
  .contact-line {
    margin: 0;
    font-size: 29px;
    font-weight: 400;
    line-height: 1.25;
  }
</style>
</head>
<body>
  <main class="canvas">
    <article class="card">
      <header class="brand">
        <span class="brand-dot" aria-hidden="true"></span>
        <span class="brand-divider" aria-hidden="true"></span>
        <h1 class="brand-name">Tolmen Brisk<br>Solutions<br>LLC</h1>
      </header>
      <section class="person">
        <p class="person-name">Lorna Tolmen</p>
        <p class="person-title">President</p>
      </section>
      <section class="contact">
        <p class="contact-phone">703-555-0148</p>
        <p class="contact-line">ltolmen@tolmenbrisksolutions.example</p>
        <p class="contact-line">www.tolmenbrisksolutions.example</p>
      </section>
    </article>
  </main>
</body>
</html>
```